Anzeigengestaltung für Online-Handel mit Edelmetallen
Zielgruppe
Online Handel mit Edelmetallen wie Gold und Silberbarren und Münzen.
Sowie der Ankauf von Gold per Postankauf
Aufgabenstellung
Ich möchte in verschiedenen Tageszeitungen in Deutschland Werbung schalten . Kleine Anzeigen etwas kleiner als Visitenkarten Größe wegen den Kosten.
Logo
Ihr Onlineshop für Edelmetalle
Vergleichen sie unsere Preis
Goldbarren / Falkenthaler
Shop.Wertkontorlo.de

```html
<!DOCTYPE html>
<html lang="de">
<head>
<meta charset="utf-8">
<title>Anzeige – Onlineshop für Edelmetalle</title>
<link rel="stylesheet" href="https://fonts.googleapis.com/css2?family=Bebas+Neue&family=Josefin+Sans:wght@400&family=Playfair+Display:wght@700&family=Poppins:wght@400&display=swap">
<style>
  :root {
    --page: #e9e9e9;
    --panel: #38383a;
    --gold: #cfa04e;
    --gold-light: #f2c23e;
    --gold-mid: #d99a24;
    --gold-dark: #9a5c18;
    --white: #ffffff;
  }
  * { margin: 0; padding: 0; box-sizing: border-box; }
  html, body {
    width: 1200px; height: 1200px; overflow: hidden;
    background: var(--page);
  }
  .ad {
    position: absolute;
    left: 109px; top: 184px;
    width: 982px; height: 832px;
    background: var(--panel);
    overflow: hidden;
    box-shadow: 0 6px 22px rgba(0,0,0,0.12);
  }
  .ad__circle {
    position: absolute;
    left: -164px; top: -208px;
    width: 488px; height: 488px;
    border-radius: 50%;
    background: var(--gold);
  }
  .ad__product {
    position: absolute;
    left: 369px; top: 102px;
    width: 605px; height: 487px;
    border-radius: 12px;
    background: radial-gradient(ellipse at 55% 45%, var(--gold-light) 0%, var(--gold-mid) 50%, var(--gold-dark) 100%);
  }
  .ad__headline {
    position: absolute;
    left: 54px; top: 48px;
    font-family: "Playfair Display", Georgia, serif;
    font-weight: 700;
    font-size: 60px;
    line-height: 81px;
    color: var(--white);
  }
  .ad__claim {
    position: absolute;
    left: 64px; top: 418px;
    font-family: "Bebas Neue", Impact, sans-serif;
    font-size: 64px;
    line-height: 75px;
    letter-spacing: 1.8px;
    color: var(--white);
  }
  .ad__shop {
    position: absolute;
    left: 51px; top: 697px;
    width: 530px; height: 75px;
  }
  .ad__shop svg { position: absolute; inset: 0; }
  .ad__shop-text {
    position: absolute;
    inset: 0;
    display: flex; align-items: center; justify-content: center;
    font-family: "Poppins", Arial, sans-serif;
    font-size: 42px;
    color: var(--white);
    padding-top: 4px;
  }
  .ad__brand {
    position: absolute;
    left: 600px; top: 722px;
    width: 372px;
    text-align: center;
    font-family: "Josefin Sans", Arial, sans-serif;
    font-size: 36px;
    color: var(--white);
  }
</style>
</head>
<body>
  <div class="ad">
    <div class="ad__circle"></div>

    <div class="ad__product" role="img" aria-label="Foto: zwei gekreuzte Feingoldbarren auf dunklem Grund"></div>

    <h1 class="ad__headline">Ihr Onlineshop<br>für Edelmetalle</h1>

    <p class="ad__claim">Vergleichen<br>Sie unsere<br>Preis!</p>

    <div class="ad__shop">
      <svg viewBox="0 0 530 75" preserveAspectRatio="none">
        <polygon points="22,2 527,2 527,53 506,73 3,73 3,21" fill="none" stroke="var(--gold)" stroke-width="4"/>
      </svg>
      <span class="ad__shop-text">Shop.Wertkontorlo.de</span>
    </div>

    <p class="ad__brand">Wertkontor-Lo.de</p>
  </div>
</body>
</html>
```